KRT business cards

I need a Business card design for my self. I am behavior analyst owner of a new company based in Miami. We offer Applied Behavior Analysis (ABA) services to individuals with developmental disabilities.

Business

```html
<!DOCTYPE html>
<html lang="en">
<head>
<meta charset="utf-8">
<title>KRT business cards</title>
<link href="https://fonts.googleapis.com/css2?family=Cinzel:wght@600&family=Open+Sans:wght@400&display=swap" rel="stylesheet">
<style>
  :root {
    --stage: #ecebe8;
    --paper: #ffffff;
    --brand-blue: #0b5fa8;
    --deep-blue: #1d3f8c;
    --leaf-green: #4ea64a;
    --ink: #3c3c3c;
    --rule: #c9c9c9;
  }
  html, body {
    margin: 0;
    width: 1200px;
    height: 1024px;
    overflow: hidden;
    background: var(--stage);
  }
  .canvas {
    position: relative;
    width: 1200px;
    height: 1024px;
  }
  .card {
    position: absolute;
    left: 250px;
    width: 700px;
    height: 400px;
    background: var(--paper);
    box-shadow: 0 6px 18px rgba(0,0,0,0.18);
    overflow: hidden;
  }
  .card-front { top: 70px; }
  .card-back { top: 554px; }

  .front-wave {
    position: absolute;
    inset: 0;
  }
  .contact-block {
    position: absolute;
    left: 56px;
    top: 48px;
    width: 380px;
  }
  .person-name {
    margin: 0;
    font-family: "Cinzel", serif;
    font-weight: 600;
    font-size: 26px;
    color: var(--brand-blue);
    letter-spacing: 0.5px;
  }
  .person-title {
    margin: 2px 0 22px;
    font-family: "Open Sans", sans-serif;
    font-size: 15px;
    color: var(--ink);
  }
  .contact-list {
    list-style: none;
    margin: 0;
    padding: 0;
    font-family: "Open Sans", sans-serif;
    font-size: 14px;
    color: var(--ink);
  }
  .contact-list li {
    display: flex;
    align-items: center;
    gap: 10px;
    margin-bottom: 8px;
  }
  .contact-list svg {
    width: 14px;
    height: 14px;
    flex: none;
    fill: var(--deep-blue);
  }
  .divider {
    position: absolute;
    left: 56px;
    top: 232px;
    width: 300px;
    height: 1px;
    background: var(--rule);
  }
  .brand {
    position: absolute;
    display: flex;
    align-items: center;
    gap: 14px;
    font-family: "Cinzel", serif;
    font-weight: 600;
    color: var(--deep-blue);
  }
  .brand-dot {
    border-radius: 50%;
    background: var(--leaf-green);
  }
  .card-front .brand {
    left: 70px;
    top: 266px;
    font-size: 56px;
  }
  .card-front .brand-dot { width: 30px; height: 30px; }
  .card-back .brand {
    left: 0;
    right: 0;
    top: 0;
    bottom: 0;
    justify-content: center;
    font-size: 96px;
  }
  .card-back .brand-dot { width: 48px; height: 48px; }
</style>
</head>
<body>
<main class="canvas">
  <section class="card card-front" aria-label="Business card front">
    <svg class="front-wave" viewBox="0 0 700 400" preserveAspectRatio="none" aria-hidden="true">
      <path d="M700 0 L640 0 C560 110 520 170 540 250 C555 320 500 370 430 400 L700 400 Z" fill="var(--leaf-green)"/>
      <path d="M700 0 L665 0 C590 110 555 175 572 255 C585 320 535 370 470 400 L700 400 Z" fill="var(--paper)"/>
      <path d="M700 0 L678 0 C605 115 575 180 590 258 C602 322 555 372 492 400 L700 400 Z" fill="var(--brand-blue)"/>
    </svg>

    <div class="contact-block">
      <h1 class="person-name">Daniel R. Moreno</h1>
      <p class="person-title">Managing Member,</p>
      <ul class="contact-list">
        <li><svg viewBox="0 0 24 24"><path d="M6.6 10.8a15 15 0 0 0 6.6 6.6l2.2-2.2a1 1 0 0 1 1-.25 11.4 11.4 0 0 0 3.6.57 1 1 0 0 1 1 1V20a1 1 0 0 1-1 1A17 17 0 0 1 3 4a1 1 0 0 1 1-1h3.5a1 1 0 0 1 1 1c0 1.25.2 2.45.57 3.57a1 1 0 0 1-.25 1z"/></svg>(305) 555-0142,</li>
        <li><svg viewBox="0 0 24 24"><path d="M6 3h10v5H6zM4 9h16a2 2 0 0 1 2 2v7h-4v3H6v-3H2v-7a2 2 0 0 1 2-2zm4 7v3h8v-3z"/></svg>(305) 555-0143,</li>
        <li><svg viewBox="0 0 24 24"><path d="M3 5h18v14H3zm2 2v.5l7 4.5 7-4.5V7z"/></svg>daniel@krtbehavior.com</li>
        <li><svg viewBox="0 0 24 24"><path d="M12 2a7 7 0 0 1 7 7c0 5-7 13-7 13S5 14 5 9a7 7 0 0 1 7-7zm0 4.5a2.5 2.5 0 1 0 0 5 2.5 2.5 0 0 0 0-5z"/></svg>2250 Harbor Lane, Miami, FL 33131,</li>
      </ul>
    </div>

    <div class="divider"></div>

    <div class="brand"><span class="brand-dot"></span>KRT</div>
  </section>

  <section class="card card-back" aria-label="Business card back">
    <div class="brand"><span class="brand-dot"></span>KRT</div>
  </section>
</main>
</body>
</html>
```